Brookvane Holdings Ltd - Logo and Business Card

Create a logo and business card design for our new company.

Canadian private investment company with holdings in Saskatchewan Oil and real-estate.

Target Market(s)

Investors

Industry/Entity Type

Finance

Contact Information for Business Card

Logo
Name - Dalton Pryce
Position - President
Phone - 306.482.7159
Website - www.brookvaneholdings.ca

Logo Text

Today. Tomorrow. Together. (Tag Line)

Colors

Designer to choose colors to be used in the design.

Requirements
Must have
• Logo Must Have - Type Font only
• Must be modern, professional and stand out from the crowd.
Nice to have
• Don't have any, blank slate.

```html
<!DOCTYPE html>
<html lang="en">
<head>
<meta charset="utf-8">
<title>Brookvane Holdings – Business Card</title>
<link href="https://fonts.googleapis.com/css2?family=Michroma&family=Arimo:wght@400;700&display=swap" rel="stylesheet">
<style>
  :root {
    --bg: #e9e6e1;
    --card: #f7f7f7;
    --card-edge: #dcdcdc;
    --brand: #2f7fa6;
    --brand-deep: #1f6384;
    --brand-light: #6fc3cf;
    --ink-light: #ffffff;
  }
  * { box-sizing: border-box; margin: 0; padding: 0; }
  html, body { width: 1200px; height: 1023px; overflow: hidden; }
  body {
    background: var(--bg);
    display: flex;
    flex-direction: column;
    align-items: center;
    justify-content: center;
    gap: 44px;
    font-family: "Arimo", Arial, sans-serif;
  }
  .card {
    position: relative;
    width: 770px;
    height: 440px;
    border-radius: 22px;
    background: linear-gradient(160deg, #ffffff 0%, var(--card) 60%, #ececec 100%);
    box-shadow: 0 2px 0 var(--card-edge), 0 10px 24px rgba(0,0,0,.15);
    overflow: hidden;
  }
  .wordmark {
    font-family: "Michroma", "Arial", sans-serif;
    color: var(--brand);
    font-weight: 400;
    display: flex;
    align-items: center;
    white-space: nowrap;
  }
  .wordmark .mark {
    display: inline-block;
    background: var(--brand);
  }

  /* front */
  .card--front { display: flex; align-items: center; justify-content: center; }
  .card--front .wordmark { font-size: 40px; gap: 22px; }
  .card--front .mark { width: 34px; height: 34px; }

  /* back */
  .card--back .wordmark {
    position: absolute;
    top: 78px;
    right: 70px;
    font-size: 22px;
    gap: 14px;
  }
  .card--back .mark { width: 20px; height: 20px; }
  .band { position: absolute; inset: 0; width: 100%; height: 100%; }
  .holder {
    position: absolute;
    right: 62px;
    top: 268px;
    text-align: right;
    color: var(--ink-light);
  }
  .holder__name { font-size: 34px; }
  .holder__role { font-size: 19px; margin-top: 4px; }
  .contacts {
    position: absolute;
    left: 52px;
    bottom: 36px;
    list-style: none;
    color: var(--ink-light);
    font-size: 16px;
    line-height: 26px;
  }
  .contacts li { display: flex; align-items: center; gap: 10px; }
  .contacts svg { width: 14px; height: 14px; flex: none; }
</style>
</head>
<body>

  <section class="card card--front">
    <div class="wordmark"><span class="mark"></span>Brookvane Holdings</div>
  </section>

  <section class="card card--back">
    <div class="wordmark"><span class="mark"></span>Brookvane Holdings</div>

    <svg class="band" viewBox="0 0 770 440" preserveAspectRatio="none" aria-hidden="true">
      <defs>
        <linearGradient id="bandFill" x1="0" y1="0" x2="1" y2="1">
          <stop offset="0" stop-color="#3a8fb3"/>
          <stop offset="1" stop-color="#1f6384"/>
        </linearGradient>
      </defs>
      <path d="M0 198 C 260 150, 560 170, 770 250 L770 440 L0 440 Z" fill="#6fc3cf"/>
      <path d="M0 208 C 260 162, 560 184, 770 264 L770 440 L0 440 Z" fill="#ffffff"/>
      <path d="M0 218 C 260 176, 560 198, 770 280 L770 440 L0 440 Z" fill="url(#bandFill)"/>
    </svg>

    <div class="holder">
      <p class="holder__name">Dalton Pryce</p>
      <p class="holder__role">President</p>
    </div>

    <ul class="contacts">
      <li><svg viewBox="0 0 14 14"><path d="M7 1a4 4 0 0 0-4 4c0 3 4 8 4 8s4-5 4-8a4 4 0 0 0-4-4zm0 5.5A1.5 1.5 0 1 1 7 3.5a1.5 1.5 0 0 1 0 3z" fill="#fff"/></svg>Your Address</li>
      <li><svg viewBox="0 0 14 14"><path d="M3 1.5l2 .2 1 3-1.3 1a7 7 0 0 0 3.6 3.6l1-1.3 3 1 .2 2-1.5 1.5C6 12 2 8 1.5 3z" fill="#fff"/></svg>306.482.7159</li>
      <li><svg viewBox="0 0 14 14"><rect x="1" y="3" width="12" height="8" fill="none" stroke="#fff" stroke-width="1.3"/><path d="M1 3l6 5 6-5" fill="none" stroke="#fff" stroke-width="1.3"/></svg>info@brookvaneholdings.ca</li>
      <li><svg viewBox="0 0 14 14"><circle cx="7" cy="7" r="5.8" fill="none" stroke="#fff" stroke-width="1.2"/><path d="M1.2 7h11.6M7 1.2c-3 3.5-3 8 0 11.6M7 1.2c3 3.5 3 8 0 11.6" fill="none" stroke="#fff" stroke-width="1.1"/></svg>www.brookvaneholdings.ca</li>
    </ul>
  </section>

</body>
</html>
```